BrightNomadRx.com Blog Design (Travel, Lifestyle, and Life Hacking blog)

I am launching a lifestyle blog about my life. I'm a doctor who travels the world trying the best restaurants, airlines and trying to have as much fun as possible. I also invest in startups, and am always trying new tricks to make life better. I also plan to write about various other topics, but essentially it is about travel, lifestyle and medicine. I need a creative and really awesome looking design for a new wordpress blog called BrightNomadRx

Target Market(s)

Physicians, Entrepreneurs, Travellers

Industry/Entity Type

Airlines

Number of Pages Required

1 page

Font styles to use
Serif

Requirements
Must have
• Slick looking graphics with a highly professional modern feel

```html
<!DOCTYPE html>
<html lang="en">
<head>
<meta charset="utf-8">
<title>BrightNomadRx — Travel, Lifestyle &amp; Medicine</title>
<link href="https://fonts.googleapis.com/css2?family=Raleway:wght@400;500;600;700&family=Lora:wght@400;500&display=swap" rel="stylesheet">
<style>
:root{
  --blue:#2f9fd6;
  --green:#2eab4a;
  --ink:#333333;
  --muted:#555555;
  --grey-btn:#5a5a5a;
  --panel:#e4e4e4;
  --hero:#f3f3f3;
  --line:#dcdcdc;
  --white:#ffffff;
}
*{box-sizing:border-box;margin:0;padding:0}
html,body{width:1200px;height:2885px;overflow:hidden;background:var(--white)}
body{position:relative;font-family:"Raleway",Arial,sans-serif;color:var(--ink)}
.abs{position:absolute}

/* header */
.follow{left:173px;top:16px;font-size:13px;color:var(--muted);display:flex;align-items:center;gap:8px}
.follow .dot{width:26px;height:26px;border-radius:50%;background:var(--blue)}
.follow .dot.grey{background:#777}
.search{left:812px;top:10px;width:211px;height:32px;border:1px solid #cfcfcf;display:flex}
.search span{flex:1;font-size:12px;color:#aaa;padding:8px 8px}
.search i{width:30px;background:var(--green);display:flex;align-items:center;justify-content:center}
.logo{left:173px;top:62px;font-size:33px;font-weight:700;color:var(--blue)}
.nav{left:502px;top:69px}
.nav a{position:absolute;top:0;height:31px;line-height:31px;text-align:center;font-size:13px;font-weight:600;color:var(--white);background:var(--grey-btn);border-radius:3px;text-decoration:none}
.nav a.active{background:var(--blue)}
.header-rule{left:0;top:117px;width:1200px;height:3px;background:#e2e2e2;box-shadow:0 2px 4px rgba(0,0,0,.12)}

/* hero */
.hero{left:0;top:120px;width:1200px;height:467px;background:var(--hero)}
.hero-art{left:560px;top:150px;width:480px;height:400px;z-index:1;background:
  radial-gradient(ellipse 110px 95px at 52% 25%,#e53a4a 0,rgba(232,120,130,.55) 60%,transparent 100%),
  radial-gradient(circle 60px at 85% 58%,#7fc640 0,rgba(160,210,120,.5) 60%,transparent 100%),
  radial-gradient(ellipse 70px 110px at 12% 62%,#c94a2c 0,rgba(225,160,110,.5) 60%,transparent 100%)}
.hero-kicker,.hero-title,.btn-know,.hero-dots{z-index:2}
.hero-kicker{left:173px;top:253px;font-size:32px;font-weight:700;color:#cfe7ee}
.hero-title{left:173px;top:309px;font-family:"Lora",Georgia,serif;font-size:28px;letter-spacing:.5px;color:#444;white-space:nowrap}
.btn-know{left:173px;top:367px;width:131px;height:39px;background:var(--blue);color:var(--white);font-weight:700;font-size:17px;text-align:center;line-height:39px;border-radius:2px}
.hero-dots{left:182px;top:433px;display:flex;gap:8px}
.hero-dots i{width:10px;height:10px;border-radius:50%;background:#555}
.hero-dots i.on{background:#9fd0e8;border:2px solid #555}

/* category cards */
.card{top:627px;width:188px;height:306px;border-radius:8px}
.card .pic{height:127px;border-radius:8px 8px 0 0}
.card .body{height:179px;border-radius:0 0 8px 8px;color:var(--white);text-align:center;padding-top:20px}
.card h3{font-size:21px;font-weight:600;letter-spacing:.5px}
.card p{font-size:11.5px;line-height:16px;padding:8px 14px 0}
.card .more{position:absolute;left:68px;bottom:-24px;width:52px;height:52px;border-radius:50%;background:var(--green);border:3px solid var(--white);color:var(--white);font-size:11px;font-weight:600;line-height:13px;text-align:center;padding-top:11px}
.card.blue .body{background:var(--blue)}
.card.green .body{background:var(--green)}

.ad{border:1px solid #bbb;border-radius:8px}

/* posts */
.post{left:173px;width:590px;height:454px}
.post .date{position:absolute;left:0;top:0;width:65px;height:67px;background:#e8e8e8;text-align:center;font-size:17px;line-height:23px;padding-top:11px;color:#444}
.post h2{position:absolute;left:85px;top:10px;font-size:24px;font-weight:500;color:var(--blue);white-space:nowrap}
.post .sub{position:absolute;left:85px;top:41px;font-size:12px;color:#444}
.post .pic{position:absolute;left:0;top:67px;width:590px;height:187px}
.post .text{position:absolute;left:0;top:262px;width:590px;font-size:12.3px;line-height:20px;color:#333}
.post .meta{position:absolute;left:0;top:380px;width:590px;height:27px;font-size:11px;color:var(--muted)}
.meta span{position:absolute;top:6px;display:flex;align-items:center;gap:7px}
.meta .readmore{position:absolute;right:0;top:0;width:88px;height:27px;background:var(--blue);color:var(--white);font-size:11px;font-weight:600;text-align:center;line-height:27px}
.post .rule{position:absolute;left:0;top:412px;width:590px;height:1px;background:var(--line)}

.load-more{left:173px;top:2783px;width:590px;height:38px;border:1px solid #999;border-radius:4px;display:flex;align-items:center;justify-content:center;gap:10px;font-size:13px;color:#555}
.footer{left:0;top:2842px;width:1200px;height:43px;background:var(--blue);color:var(--white);font-size:12px;text-align:center;line-height:43px}

/* sidebar */
.panel{background:var(--panel)}
.signup{left:783px;top:952px;width:246px;height:183px;padding:16px 20px}
.signup p{font-size:13px;font-weight:600;line-height:21px;color:#333}
.field{background:var(--white);border:1px solid #999;height:31px;font-size:11px;font-style:italic;color:#999;padding:8px 8px}
.signup .field{margin-top:14px;width:204px}
.btn-s{display:inline-block;background:var(--blue);color:var(--white);font-size:11px;font-weight:600;height:27px;line-height:27px;padding:0 12px;margin-top:26px}
.side-h{font-size:25px;font-weight:600;color:#222}
.recent-h{left:787px;top:1160px}
.recent{left:783px;top:1202px;width:246px;height:211px;padding:6px 10px 0 14px}
.recent li{list-style:none;font-size:11px;line-height:19px;color:#444;padding-left:16px;position:relative;border-bottom:1px solid #f3f3f3;padding-bottom:2px;margin-bottom:2px}
.recent li::before{content:"";position:absolute;left:0;top:7px;width:5px;height:5px;border-right:2px solid var(--green);border-bottom:2px solid var(--green);transform:rotate(-45deg)}
.recent li:last-child{border:0}
.view-all{left:965px;top:1381px;width:60px;height:24px;background:var(--blue);color:var(--white);font-size:11px;font-weight:600;text-align:center;line-height:24px}
.social{left:783px;top:1437px;width:246px;height:332px;border:1px solid #ddd;overflow:hidden}
.tabs{display:flex;height:30px;background:#eee;font-size:10.5px}
.tabs div{display:flex;align-items:center;gap:4px;padding:0 5px;white-space:nowrap}
.tabs div.on{background:var(--white)}
.tabs i{width:13px;height:13px;border-radius:50%;border:1px solid #666}
.feed-item{display:flex;gap:10px;padding:12px 10px 0 10px;height:72px}
.avatar{width:50px;height:50px;flex:none}
.feed-item p{font-size:11px;line-height:17px;color:#444}
.like{display:inline-block;border:1px solid #9ab;border-radius:2px;font-size:9px;color:#3b5a98;padding:0 5px;margin-top:2px}
.query{left:783px;top:1800px;width:246px;height:238px;padding:12px 20px}
.query .side-h{font-size:21px}
.query .field{width:206px;margin-top:10px}
.query .field.tall{height:78px}
.btn-send{display:inline-block;background:var(--green);color:var(--white);font-size:11px;font-weight:600;height:31px;line-height:31px;padding:0 22px;margin-top:16px}
.tags-h{left:787px;top:2085px}
.tags{left:783px;top:2125px;width:246px;height:179px;padding:12px 10px;font-size:19px;line-height:29px;color:#333}
.tags span{margin-right:4px}
.t-s{font-size:12px}.t-m{font-size:16px}.t-l{font-size:21px}
</style>
</head>
<body>

<header>
  <div class="abs follow">Follow Us On <i class="dot"></i><i class="dot"></i><i class="dot grey"></i></div>
  <div class="abs search"><span>Search here</span><i><svg width="16" height="16" viewBox="0 0 16 16"><circle cx="7" cy="7" r="5" fill="none" stroke="#fff" stroke-width="2"/><line x1="11" y1="11" x2="15" y2="15" stroke="#fff" stroke-width="2"/></svg></i></div>
  <div class="abs logo">BrightNomadRx</div>
  <nav class="abs nav">
    <a class="active" style="left:0;width:56px">Home</a>
    <a style="left:84px;width:60px">Travel</a>
    <a style="left:173px;width:69px">Lifestyle</a>
    <a style="left:252px;width:79px">Medicine</a>
    <a style="left:340px;width:77px">About</a>
    <a style="left:435px;width:90px">Contact Us</a>
  </nav>
  <div class="abs header-rule"></div>
</header>

<section class="abs hero"></section>
<div class="abs hero-art" role="img" aria-label="Stacked vegetables wrapped in a tape measure, a red heart with a pulse line, a green apple and a stethoscope"></div>
<div class="abs hero-kicker">BrightNomadRx</div>
<div class="abs hero-title">NUTRITION &amp; EXERCISE</div>
<div class="abs btn-know">KNOW MORE</div>
<div class="abs hero-dots"><i></i><i class="on"></i><i></i><i></i></div>

<section>
  <article class="abs card blue" style="left:173px">
    <div class="pic" role="img" aria-label="Travel flat lay with map, camera and coffee" style="background:linear-gradient(135deg,#a9b7bf,#6e8692)"></div>
    <div class="body"><h3>TRAVEL</h3><p>Lorem ipsum dolor sit amet, consectetuer adipiscing elit, sed diam nonummy nibh euismod.</p></div>
    <div class="more">Read<br>More</div>
  </article>
  <article class="abs card green" style="left:373px">
    <div class="pic" role="img" aria-label="Family running together on a sunny beach" style="background:linear-gradient(180deg,#8fc6e6,#cfe3ea 55%,#e5d8bd)"></div>
    <div class="body"><h3>LIFESTYLE</h3><p>Lorem ipsum dolor sit amet, consectetuer adipiscing elit, sed diam nonummy nibh euismod.</p></div>
    <div class="more">Read<br>More</div>
  </article>
  <article class="abs card blue" style="left:575px">
    <div class="pic" role="img" aria-label="Doctor with floating medical icons" style="background:linear-gradient(135deg,#eef3f6,#b9cfdd)"></div>
    <div class="body"><h3>MEDICINE</h3><p>Lorem ipsum dolor sit amet, consectetuer adipiscing elit, sed diam nonummy nibh euismod.</p></div>
    <div class="more">Read<br>More</div>
  </article>
  <div class="abs ad" style="left:783px;top:627px;width:246px;height:296px;background:radial-gradient(circle at 50% 58%,#c9443f 0,#e9b4a8 28%,#ffffff 50%)" role="img" aria-label="Nutrition month poster with a heart-shaped plate of food lifting a dumbbell"></div>
</section>

<main>
  <article class="abs post" style="top:973px">
    <div class="date">02<br>JAN</div>
    <h2>Lorem ipsum dolor sit amet, consecit adipi</h2>
    <div class="sub">Duis aute irure dolor in reprehenderit</div>
    <div class="pic" role="img" aria-label="Suspension bridge over a bay at sunset" style="background:linear-gradient(180deg,#c6a7c9 0,#f1a56b 45%,#7d6a8a 70%,#5a6f8c)"></div>
    <p class="text">Lorem ipsum dolor sit amet, consect adipiscing elit, sed do eiusmod tempor incidimen labore n dolorme laboris ni ut aliquip ex ena lin consequat Duis aute irure dolor in reprehenderit magna aliqua. Ut enim ad qnexercitation ullamco Neque porro quisquam est, qui dolorem ipsum quia dolor sit amet, conadipi velit sed quia non numquam eius modi tempora incidunt. Quis autem vel eum iure repreminderit in voluptate velit esse quam nihil molestiae consequatur.</p>
    <div class="meta">
      <span style="left:0"><svg width="13" height="13" viewBox="0 0 13 13"><rect x="1" y="2" width="10" height="10" fill="none" stroke="#2eab4a" stroke-width="1.5"/><line x1="5" y1="8" x2="12" y2="1" stroke="#2eab4a" stroke-width="2"/></svg>Admin</span>
      <span style="left:115px"><svg width="14" height="12" viewBox="0 0 14 12"><ellipse cx="7" cy="5" rx="6.5" ry="4.5" fill="#2eab4a"/><path d="M3 8 L2 12 L7 9Z" fill="#2eab4a"/></svg>Leave A Comment</span>
      <span style="left:290px"><svg width="13" height="13" viewBox="0 0 13 13"><rect x="0" y="6" width="3" height="7" fill="#2eab4a"/><path d="M4 6 L7 1 Q9 1 8 5 L12 5 Q13 6 12 8 L11 12 L4 12Z" fill="#2eab4a"/></svg>Like Us</span>
      <span style="left:408px"><svg width="13" height="13" viewBox="0 0 13 13"><circle cx="10" cy="2.5" r="2.2" fill="#2eab4a"/><circle cx="2.5" cy="6.5" r="2.2" fill="#2eab4a"/><circle cx="10" cy="10.5" r="2.2" fill="#2eab4a"/><path d="M10 2.5 L2.5 6.5 L10 10.5" fill="none" stroke="#2eab4a" stroke-width="1.2"/></svg>Share</span>
      <div class="readmore">READ MORE</div>
    </div>
    <div class="rule"></div>
  </article>

  <article class="abs post" style="top:1427px">
    <div class="date">02<br>JAN</div>
    <h2>Lorem ipsum dolor sit amet</h2>
    <div class="sub">Duis aute irure dolor in reprehenderit</div>
    <div class="pic" role="img" aria-label="Traveller working on a laptop on a mountain top above the clouds" style="background:linear-gradient(180deg,#5d86b3 0,#a9c2d8 45%,#3e6a94 65%,#3b3834)"></div>
    <p class="text">Lorem ipsum dolor sit amet, consect adipiscing elit, sed do eiusmod tempor incidimen labore n dolorme laboris ni ut aliquip ex ena lin consequat Duis aute irure dolor in reprehenderit magna aliqua. Ut enim ad qnexercitation ullamco Neque porro quisquam est, qui dolorem ipsum quia dolor sit amet, conadipi velit sed quia non numquam eius modi tempora incidunt. Quis autem vel eum iure repreminderit in voluptate velit esse quam nihil molestiae consequatur.</p>
    <div class="meta">
      <span style="left:0"><svg width="13" height="13" viewBox="0 0 13 13"><rect x="1" y="2" width="10" height="10" fill="none" stroke="#2eab4a" stroke-width="1.5"/><line x1="5" y1="8" x2="12" y2="1" stroke="#2eab4a" stroke-width="2"/></svg>Admin</span>
      <span style="left:115px"><svg width="14" height="12" viewBox="0 0 14 12"><ellipse cx="7" cy="5" rx="6.5" ry="4.5" fill="#2eab4a"/><path d="M3 8 L2 12 L7 9Z" fill="#2eab4a"/></svg>Leave A Comment</span>
      <span style="left:290px"><svg width="13" height="13" viewBox="0 0 13 13"><rect x="0" y="6" width="3" height="7" fill="#2eab4a"/><path d="M4 6 L7 1 Q9 1 8 5 L12 5 Q13 6 12 8 L11 12 L4 12Z" fill="#2eab4a"/></svg>Like Us</span>
      <span style="left:408px"><svg width="13" height="13" viewBox="0 0 13 13"><circle cx="10" cy="2.5" r="2.2" fill="#2eab4a"/><circle cx="2.5" cy="6.5" r="2.2" fill="#2eab4a"/><circle cx="10" cy="10.5" r="2.2" fill="#2eab4a"/><path d="M10 2.5 L2.5 6.5 L10 10.5" fill="none" stroke="#2eab4a" stroke-width="1.2"/></svg>Share</span>
      <div class="readmore">READ MORE</div>
    </div>
    <div class="rule"></div>
  </article>

  <article class="abs post" style="top:1881px">
    <div class="date">05<br>JAN</div>
    <h2>Lorem ipsum dolor sit amet, consecit adipi</h2>
    <div class="sub">Duis aute irure dolor in reprehenderit</div>
    <div class="pic" role="img" aria-label="Fresh vegetables around a heart-shaped chalkboard sign about mindful eating" style="background:radial-gradient(circle at 45% 40%,#3a3a3a 0,#3a3a3a 14%,transparent 22%),linear-gradient(90deg,#3f6b2a,#8aa744 40%,#c9502e 75%,#6f8d36)"></div>
    <p class="text">Lorem ipsum dolor sit amet, consect adipiscing elit, sed do eiusmod tempor incidimen labore n dolorme laboris ni ut aliquip ex ena lin consequat Duis aute irure dolor in reprehenderit magna aliqua. Ut enim ad qnexercitation ullamco Neque porro quisquam est, qui dolorem ipsum quia dolor sit amet, conadipi velit sed quia non numquam eius modi tempora incidunt. Quis autem vel eum iure repreminderit in voluptate velit esse quam nihil molestiae consequatur.</p>
    <div class="meta">
      <span style="left:0"><svg width="13" height="13" viewBox="0 0 13 13"><rect x="1" y="2" width="10" height="10" fill="none" stroke="#2eab4a" stroke-width="1.5"/><line x1="5" y1="8" x2="12" y2="1" stroke="#2eab4a" stroke-width="2"/></svg>Admin</span>
      <span style="left:115px"><svg width="14" height="12" viewBox="0 0 14 12"><ellipse cx="7" cy="5" rx="6.5" ry="4.5" fill="#2eab4a"/><path d="M3 8 L2 12 L7 9Z" fill="#2eab4a"/></svg>Leave A Comment</span>
      <span style="left:290px"><svg width="13" height="13" viewBox="0 0 13 13"><rect x="0" y="6" width="3" height="7" fill="#2eab4a"/><path d="M4 6 L7 1 Q9 1 8 5 L12 5 Q13 6 12 8 L11 12 L4 12Z" fill="#2eab4a"/></svg>Like Us</span>
      <span style="left:408px"><svg width="13" height="13" viewBox="0 0 13 13"><circle cx="10" cy="2.5" r="2.2" fill="#2eab4a"/><circle cx="2.5" cy="6.5" r="2.2" fill="#2eab4a"/><circle cx="10" cy="10.5" r="2.2" fill="#2eab4a"/><path d="M10 2.5 L2.5 6.5 L10 10.5" fill="none" stroke="#2eab4a" stroke-width="1.2"/></svg>Share</span>
      <div class="readmore">READ MORE</div>
    </div>
    <div class="rule"></div>
  </article>

  <article class="abs post" style="top:2335px">
    <div class="date">10<br>JAN</div>
    <h2>Lorem ipsum dolor sit amet, consec</h2>
    <div class="sub">Duis aute irure dolor in reprehenderit</div>
    <div class="pic" role="img" aria-label="Hiker with raised arms on a rock overlooking a green valley at sunrise" style="background:linear-gradient(180deg,#e9ecd8 0,#f2efc8 30%,#8fb25a 55%,#3f6a2a 80%,#6b6a5a)"></div>
    <p class="text">Lorem ipsum dolor sit amet, consect adipiscing elit, sed do eiusmod tempor incidimen labore n dolorme laboris ni ut aliquip ex ena lin consequat Duis aute irure dolor in reprehenderit magna aliqua. Ut enim ad qnexercitation ullamco Neque porro quisquam est, qui dolorem ipsum quia dolor sit amet, conadipi velit sed quia non numquam eius modi tempora incidunt. Quis autem vel eum iure repreminderit in voluptate velit esse quam nihil molestiae consequatur.</p>
    <div class="meta">
      <span style="left:0"><svg width="13" height="13" viewBox="0 0 13 13"><rect x="1" y="2" width="10" height="10" fill="none" stroke="#2eab4a" stroke-width="1.5"/><line x1="5" y1="8" x2="12" y2="1" stroke="#2eab4a" stroke-width="2"/></svg>Admin</span>
      <span style="left:115px"><svg width="14" height="12" viewBox="0 0 14 12"><ellipse cx="7" cy="5" rx="6.5" ry="4.5" fill="#2eab4a"/><path d="M3 8 L2 12 L7 9Z" fill="#2eab4a"/></svg>Leave A Comment</span>
      <span style="left:290px"><svg width="13" height="13" viewBox="0 0 13 13"><rect x="0" y="6" width="3" height="7" fill="#2eab4a"/><path d="M4 6 L7 1 Q9 1 8 5 L12 5 Q13 6 12 8 L11 12 L4 12Z" fill="#2eab4a"/></svg>Like Us</span>
      <span style="left:408px"><svg width="13" height="13" viewBox="0 0 13 13"><circle cx="10" cy="2.5" r="2.2" fill="#2eab4a"/><circle cx="2.5" cy="6.5" r="2.2" fill="#2eab4a"/><circle cx="10" cy="10.5" r="2.2" fill="#2eab4a"/><path d="M10 2.5 L2.5 6.5 L10 10.5" fill="none" stroke="#2eab4a" stroke-width="1.2"/></svg>Share</span>
      <div class="readmore">READ MORE</div>
    </div>
    <div class="rule"></div>
  </article>

  <div class="abs load-more"><svg width="16" height="16" viewBox="0 0 16 16"><circle cx="8" cy="8" r="5" fill="none" stroke="#999" stroke-width="3" stroke-dasharray="3 2"/></svg>Load more blog</div>
</main>

<aside>
  <div class="abs panel signup">
    <p>Sign Up To Get Exclusive Lorem Ipsum Dolor Sit Amet, Consecit Adipiscing Elit</p>
    <div class="field">Enter your email address</div>
    <div class="btn-s">SIGN UP</div>
  </div>

  <h3 class="abs side-h recent-h">Recent Posts</h3>
  <ul class="abs panel recent">
    <li>Lorem ipsum dolor sit amet, consecit adipiscing elit</li>
    <li>Lorem ipsum dolor sit amet, consecit adipiscing elit</li>
    <li>Lorem ipsum dolor sit amet, consecit adipiscing elit</li>
    <li>Lorem ipsum dolor sit amet, consecit adipiscing elit</li>
  </ul>
  <div class="abs view-all">VIEW ALL</div>

  <div class="abs social">
    <div class="tabs"><div class="on"><i></i>Friendbook</div><div><i></i>Chirper</div><div><i></i>Snapgram</div></div>
    <div class="feed-item"><div class="avatar" role="img" aria-label="Reader profile photo" style="background:#c9a48a"></div><p>Lorem Ipsum is simply dummy text of the printing..<br><span class="like">Like</span></p></div>
    <div class="feed-item"><div class="avatar" role="img" aria-label="Reader profile photo" style="background:#6b4a3e"></div><p>Lorem Ipsum is simply dummy text of the printing..<br><span class="like">Like</span></p></div>
    <div class="feed-item"><div class="avatar" role="img" aria-label="Reader profile photo" style="background:#d8c2a8"></div><p>Lorem Ipsum is simply dummy text of the printing..<br><span class="like">Like</span></p></div>
    <div class="feed-item"><div class="avatar" role="img" aria-label="Reader profile photo" style="background:#5a3f36"></div><p>Lorem Ipsum is simply dummy text of the printing..<br><span class="like">Like</span></p></div>
  </div>

  <div class="abs panel query">
    <h3 class="side-h">Send Us Your Query</h3>
    <div class="field">Enter your name</div>
    <div class="field">Enter your email address</div>
    <div class="field tall">Enter your query</div>
    <div class="btn-send">SEND</div>
  </div>

  <h3 class="abs side-h tags-h">Tags</h3>
  <div class="abs panel tags">
    <span class="t-m">Health</span><span class="t-m">Health food</span><span class="t-s">friday</span>
    <span class="t-s">monday</span><span class="t-m">Diets</span><span class="t-s">Health Facts</span>
    <span class="t-l">Eat</span><span class="t-s">wednesday</span><span class="t-m">motivational</span>
    <span class="t-m">Cleanes</span><span class="t-m">Loose it</span><span class="t-l">Obesity</span>
    <span class="t-m">Fast diets</span><span class="t-l">Workouts</span><span class="t-s">Spinach</span>
  </div>

  <div class="abs ad" style="left:783px;top:2335px;width:246px;height:296px;background:radial-gradient(ellipse at 50% 45%,#5f8f2a 0,#a7c96a 26%,#ffffff 46%)" role="img" aria-label="Skincare advertisement with a halved avocado promising soothed skin"></div>
</aside>

<footer class="abs footer">Copyright© 2017 BrightNomadRx. All rights reserved.</footer>

</body>
</html>
```